Indian Takeaway Menu -

I would like to have double parallel fold A4 sheet menu.
A4 sheet cut in half and attached to the other half to make the sheet 4 small pages long.

Colors
abd036
ffffff

Requirements
Must have
• Please check new attachments - menu size and layout is not correct.
• I would like to add Dark brown colour. A4 sheet folded 4x Menu layout pocket size.
Nice to have
• Dark Brown - Parrot Green and very light Brown

```html
<!DOCTYPE html>
<html lang="en">
<head>
<meta charset="utf-8">
<title>Masala Hearth – Takeaway Menu</title>
<link rel="stylesheet" href="https://fonts.googleapis.com/css2?family=Oswald:wght@500&family=Open+Sans:wght@400;600&family=Libre+Baskerville:wght@400;700&display=swap">
<style>
:root{
  --green:#9ccb3b;
  --green-dark:#86b52c;
  --ink:#1d1d1d;
  --muted:#555;
  --red:#d7262c;
  --brown:#5a3a22;
  --paper:#ffffff;
  --backdrop:#ece4d8;
}
*{box-sizing:border-box;margin:0;padding:0}
html,body{width:1200px;height:1200px;overflow:hidden;background:var(--backdrop);font-family:"Open Sans",sans-serif;color:var(--ink)}
.strip{position:absolute;left:20px;width:1160px;height:410px;background:var(--paper);box-shadow:0 4px 14px rgba(60,40,20,.18)}
.strip--outer{top:150px}
.strip--inner{top:660px}
.panel{position:absolute;top:0;height:100%}
.ribbon{display:block;margin:0 auto;width:max-content;min-width:170px;padding:3px 26px;background:var(--green);color:#fff;font-family:"Oswald",sans-serif;font-weight:500;font-size:16px;text-align:center;clip-path:polygon(0 0,100% 0,94% 50%,100% 100%,0 100%,6% 50%);letter-spacing:.2px}
.ribbon--sm{font-size:13px;min-width:180px;padding:2px 24px}
.row{display:flex;align-items:baseline;gap:4px}
.row .name{white-space:nowrap}
.row .lead{flex:1;border-bottom:1px solid #999;transform:translateY(-3px)}
.row .price{white-space:nowrap}
.desc{color:var(--muted)}
.photo{border-radius:2px}
/* set meals */
.setmeals{left:0;width:280px;padding:22px 30px 0 36px}
.set{margin-bottom:14px}
.set .row{font-size:11px;font-weight:600}
.set ul{list-style:none;display:grid;grid-template-columns:1fr 1fr;column-gap:8px;margin-top:4px}
.set li{font-size:8px;line-height:15.5px;color:#333}
.setmeals .photo{width:172px;height:92px;margin:2px 0 0 28px;border:3px solid var(--green);background:radial-gradient(ellipse at 45% 55%,#f3d27a,#d89a3c 60%,#6e4a2a)}
/* meal deals */
.deals{left:282px;width:298px;padding-top:24px}
.deals .ribbon{min-width:220px}
.deals .body{padding:12px 0 0 15px;width:276px}
.lowfat{font-size:9px;color:var(--red);font-style:italic}
.choose{font-size:12.5px;margin:4px 0 6px}
.deal{margin-bottom:9px}
.deal .row{font-size:10.5px}
.deal .desc{font-size:7.5px;line-height:10px;margin-top:3px;width:200px}
.hours{position:absolute;left:0;bottom:0;width:298px;height:110px;background:var(--green);color:#fff;padding:8px 8px 0 8px}
.hours h3{font-weight:400;font-size:16px}
.hours p{font-size:10.5px;line-height:15px;padding-left:3px}
.hours small{display:block;font-size:6.5px;margin-top:3px;padding-left:3px}
.hours .phones{position:absolute;right:14px;top:8px;font-size:11px;line-height:22px;text-align:left}
.hours .phones svg{vertical-align:-1px;margin-right:3px}
/* cover */
.cover{left:580px;width:295px;background:linear-gradient(#f4f4f4,#ffffff 40%,#f2f2f2)}
.brand{position:absolute;top:28px;left:0;width:100%;text-align:center;font-family:"Open Sans",sans-serif;font-weight:600;font-size:13px;color:var(--brown);display:flex;justify-content:center;align-items:center;gap:6px}
.brand i{width:9px;height:9px;background:var(--red);border-radius:50%;display:inline-block}
.cover .photo{position:absolute;left:128px;top:82px;width:150px;height:240px;background:radial-gradient(ellipse at 55% 35%,#d93025 0,#b33a1c 25%,#8a5a3a 50%,#f6f3ef 78%)}
.tagline{position:absolute;left:16px;top:178px;font-family:"Libre Baskerville",serif;line-height:1}
.tagline .a{font-size:10px;letter-spacing:.5px;color:#444}
.tagline .b{font-size:25px;font-weight:700;color:var(--red);line-height:22px}
.tagline .c{font-size:16px;font-weight:700;color:var(--green);letter-spacing:.5px}
.tagline .d{font-size:10px;letter-spacing:.5px;color:#444}
.web{position:absolute;bottom:24px;width:100%;text-align:center;font-family:"Libre Baskerville",serif;font-size:10.5px;letter-spacing:4.5px;color:#333}
/* healthy sides */
.sides{left:875px;width:285px;padding-top:22px}
.sides .list{padding:10px 44px 0 22px}
.side{margin-bottom:7px}
.side .row{font-size:11px}
.side .desc{font-size:5.8px;line-height:7.5px;width:150px}
.key{position:absolute;left:22px;bottom:26px;font-size:7px;line-height:11px;color:#333}
.sides .photo{position:absolute;right:24px;bottom:20px;width:126px;height:46px;background:linear-gradient(90deg,#c9a27a,#c5562b 60%,#e6e0d5)}
/* inner strip */
.inner{padding-top:20px}
.inner .ribbon{font-size:14px;min-width:190px;padding:2px 28px}
.cols{display:grid;gap:0 12px;margin-top:10px}
.item{margin-bottom:6px}
.item .row{font-size:8px;font-weight:600}
.item .row .lead{border-color:#bbb}
.item .desc{font-size:5px;line-height:6.6px;margin-top:1px}
.starters{left:0;width:288px;padding-left:18px;padding-right:6px}
.starters .cols{grid-template-columns:1fr 1fr}
.starters .pics{display:flex;flex-direction:column;gap:8px;margin-top:8px;padding-left:10px}
.starters .pics .photo{width:92px;height:62px;background:linear-gradient(135deg,#e8d7a8,#c7983d 60%,#f1ece2)}
.curries{left:288px;width:298px;padding-right:6px;padding-left:10px}
.curries .cols{grid-template-columns:1fr 1fr;gap:0 14px}
.curries .photo{width:118px;height:78px;margin-top:6px}
.curries .p1{background:radial-gradient(ellipse at 50% 55%,#b5522a,#7b3a1f 55%,#e7e3da)}
.curries .p2{background:radial-gradient(ellipse at 55% 45%,#d4692d,#3d3b3a 60%,#ece6da)}
.lamb{left:586px;width:290px;padding-left:14px;padding-right:10px}
.lamb .cols{grid-template-columns:1fr 1fr;gap:0 12px}
.lamb .photo{width:118px;height:62px;margin-top:2px;background:radial-gradient(ellipse at 45% 50%,#d9693a,#5e4636 60%,#3b3a38)}
.prawn{margin-top:8px}
.prawn .photo{width:120px;height:60px;background:linear-gradient(90deg,#3a3530,#c85b2a 60%,#5b4a3d)}
.veg{left:876px;width:284px;padding-left:12px;padding-right:14px}
.veg .cols{grid-template-columns:1fr 1fr;gap:0 12px}
.nan{margin-top:14px;padding-left:8px}
.nan h4{font-weight:400;color:var(--green-dark);font-size:10.5px;line-height:14px;margin-top:8px}
.nan .list{width:222px;margin-top:5px}
.nan .row{font-size:8.6px;line-height:11.3px}
.nan .row .lead{border-color:#999}
</style>
</head>
<body>

<section class="strip strip--outer">
  <div class="panel setmeals">
    <div class="set">
      <div class="row"><span class="name">Set Meal 1</span><span class="lead"></span><span class="price">€16</span></div>
      <ul><li>- Onion bhajia</li><li>- Pilau rice</li><li>- Chicken Tikka Masala</li><li>- Naan</li><li>- Poppadoms</li></ul>
    </div>
    <div class="set">
      <div class="row"><span class="name">Set Meal 2</span><span class="lead"></span><span class="price">€27</span></div>
      <ul><li>- Onion bhajia</li><li>- 2xPilau rice</li><li>- Chicken tikka</li><li>- 1xNaan</li><li>- Chicken Tikka Masala</li><li>- Poppadom</li><li>- Lamb Roganjosh</li></ul>
    </div>
    <div class="set">
      <div class="row"><span class="name">Set Meal 3/4</span><span class="lead"></span><span class="price">€43</span></div>
      <ul><li>- Onion bhajia</li><li>- Sambhar Veg Curry</li><li>- Vegetable samosa</li><li>- 2 x Pilau Rice</li><li>- Chicken tikka</li><li>- 2 x Naan</li><li>- Chicken Tikka Masala</li><li>- Poppadom</li><li>- Lamb Roganjosh</li></ul>
    </div>
    <div class="photo" role="img" aria-label="Photo of a golden garlic naan bread on a plate"></div>
  </div>

  <div class="panel deals">
    <span class="ribbon">Meal Deals only €8.50</span>
    <div class="body">
      <p class="lowfat">(Low Fat Dishes)</p>
      <p class="choose">Choose with Rice or Plain Naan</p>
      <div class="deal"><div class="row"><span class="name">Chicken Dupiaza</span><span class="lead"></span><span class="price">€8.50</span></div><p class="desc">Chicken cooked with ginger and chunks of onions and finished with onion seeds....</p></div>
      <div class="deal"><div class="row"><span class="name">Chicken Rogan josh</span><span class="lead"></span><span class="price">€8.50</span></div><p class="desc">A red chicken curry prepared with fresh herb &amp; spices, a delicacy from Kashmir</p></div>
      <div class="deal"><div class="row"><span class="name">Chicken Bhuna</span><span class="lead"></span><span class="price">€8.50</span></div><p class="desc">Tomatoes and onion sauce cooked with black peppers &amp; spring onions.</p></div>
      <div class="deal"><div class="row"><span class="name">Tarkari Makhani</span><span class="lead"></span><span class="price">€8.50</span></div><p class="desc">Mixed seasonal vegetables in a smooth tikka masala sauce</p></div>
    </div>
    <div class="hours">
      <h3>Opening Hours:</h3>
      <p>Sun - Thurs 5PM to 10.00PM<br>Fri - Sat 5.00PM-10.30PM<br>Deliveries From 5.30PM</p>
      <small>All our meals are cooked to order.</small>
      <div class="phones">
        <div><svg width="9" height="9" viewBox="0 0 24 24" fill="#fff"><path d="M6.6 10.8a15 15 0 0 0 6.6 6.6l2.2-2.2a1 1 0 0 1 1-.25 11.4 11.4 0 0 0 3.6.57 1 1 0 0 1 1 1V20a1 1 0 0 1-1 1A17 17 0 0 1 3 4a1 1 0 0 1 1-1h3.5a1 1 0 0 1 1 1c0 1.25.2 2.45.57 3.6a1 1 0 0 1-.25 1z"/></svg>015550184</div>
        <div style="padding-left:12px">015550186</div>
      </div>
    </div>
  </div>

  <div class="panel cover">
    <div class="brand"><i></i>Masala Hearth</div>
    <div class="photo" role="img" aria-label="Photo of stacked wooden bowls with red chillies and ground spices"></div>
    <div class="tagline">
      <div class="a">AUTHENTIC</div>
      <div class="b">INDIAN<br>FOOD</div>
      <div class="c">DELIVERED</div>
      <div class="d">TO YOU AT HOME</div>
    </div>
    <div class="web">www.masalahearth.ie</div>
  </div>

  <div class="panel sides">
    <span class="ribbon">Healthy Side orders</span>
    <div class="list">
      <div class="side"><div class="row"><span class="name">Sautéed Broccoli</span><span class="lead"></span><span class="price">€5</span></div><p class="desc">Broccoli, green beans and spinach leaves sautéed with roasted cumin and fresh garlic.</p></div>
      <div class="side"><div class="row"><span class="name">Chana Saag</span><span class="lead"></span><span class="price">€5</span></div><p class="desc">Chickpeas cooked with chopped spinach, onion, and cumin and finished with cream</p></div>
      <div class="side"><div class="row"><span class="name">Chana Masala &nbsp;v</span><span class="lead"></span><span class="price">€5</span></div><p class="desc">Chickpeas simmered with tomato, caramelised onion, black pepper and fresh coriander.</p></div>
      <div class="side"><div class="row"><span class="name">Aloo Saag &nbsp;&nbsp;3 yv</span><span class="lead"></span><span class="price">€5</span></div><p class="desc">Crispy Potato with spinach, caramelised onion, garam masala and a dash of cream.</p></div>
      <div class="side"><div class="row"><span class="name">Sautéed Broccoli</span><span class="lead"></span><span class="price">€5</span></div><p class="desc">Broccoli, green beans and spinach leaves sautéed with roasted cumin and fresh garlic.</p></div>
      <div class="side"><div class="row"><span class="name">Aloo Ghobhi &nbsp;&nbsp;v</span><span class="lead"></span><span class="price">€5</span></div><p class="desc">Crispy Potatoes cubes &amp; Cauliflower cooked with roasted cumin with tomato and onion</p></div>
      <div class="side"><div class="row"><span class="name">Tarka Daal &nbsp;4 y v</span><span class="lead"></span><span class="price">€5</span></div><p class="desc">Home style soaked yellow chana cooked with cumin &amp; garam masala.</p></div>
      <div class="side"><div class="row"><span class="name">Tangy Aloo &nbsp;&nbsp;&nbsp;&nbsp;v</span><span class="lead"></span><span class="price">€5</span></div><p class="desc">Crispy Potatoes cubes cooked with roasted cumin and touch of our tangy sauce</p></div>
    </div>
    <div class="key">Y: can be cooked without allergen<br>H: Healthy Option<br>V: Suitable for Vegans</div>
    <div class="photo" role="img" aria-label="Photo of a curry dish with naan on a wooden table"></div>
  </div>
</section>

<section class="strip strip--inner">
  <div class="panel inner starters">
    <span class="ribbon">Starters</span>
    <div class="cols">
      <div>
        <div class="item"><div class="row"><span class="name">Onion Bhajia</span><span class="lead"></span><span class="price">€4.5</span></div><p class="desc">Spinach &amp; onions fritters flavored with mild spices</p></div>
        <div class="item"><div class="row"><span class="name">Vegetable Samosa 2</span><span class="lead"></span><span class="price">€4.5</span></div><p class="desc">Crispy Pastry stuffed with potatoes, chick peas, green peas mixed with desi spices until golden.</p></div>
        <div class="item"><div class="row"><span class="name">Palak Tikki</span><span class="lead"></span><span class="price">€4.5</span></div><p class="desc">Cakes of fresh spinach and chana dal</p></div>
        <div class="item"><div class="row"><span class="name">Veg Pakora</span><span class="lead"></span><span class="price">€5</span></div><p class="desc">Cauliflower, potato and broccoli, golden fried with Gram flour batter</p></div>
        <div class="item"><div class="row"><span class="name">Keema Singhara 2</span><span class="lead"></span><span class="price">€5</span></div><p class="desc">Spicy seasoned mince lamb in light pastry</p></div>
        <div class="item"><div class="row"><span class="name">Chicken Tikka 3</span><span class="lead"></span><span class="price">€5</span></div><p class="desc">Tender chicken marinated overnight with yoghurt, spices charred in tandoor</p></div>
        <div class="item"><div class="row"><span class="name">Doner Kebab 2,3,6</span><span class="lead"></span><span class="price">€5</span></div><p class="desc">Stripes of minced chicken &amp; beef served with garlic mayo, chilli sauce &amp; mixed salad &amp; wrapped in naan.</p></div>
        <div class="item"><div class="row"><span class="name">Chicken Tikka Kebab</span><span class="lead"></span><span class="price">€5</span></div><p class="desc">Chicken breast marinated in spices, barbecued served with garlic mayo, chilli sauce &amp; mixed salad &amp; wrapped in naan</p></div>
        <div class="item"><div class="row"><span class="name">Seekh Kebab</span><span class="lead"></span><span class="price">€5.5</span></div><p class="desc">Skewered hand pounded lamb glazed in tandoor with green chilli &amp; black cardamom</p></div>
      </div>
      <div>
        <div class="item"><div class="row"><span class="name">Chicken Pakora</span><span class="lead"></span><span class="price">€5</span></div><p class="desc">Boneless pieces of chicken coated in gram flour batter, with spices.</p></div>
        <div class="item"><div class="row"><span class="name">Chicken Wings &nbsp;2,1</span><span class="lead"></span><span class="price">€9.5</span></div></div>
        <div class="item"><div class="row"><span class="name">Tandoori Mix Meat Platter 3</span><span class="lead"></span><span class="price">€5</span></div><p class="desc">Our special tandoori assortment of tandoori chicken on bone, seekh kebab and chicken tikka.</p></div>
        <div class="item"><div class="row"><span class="name">Mix Veg platter 2</span><span class="lead"></span><span class="price">€5</span></div><p class="desc">Veg Samosa, Onion Bhaji, Veg Pakora</p></div>
        <div class="item"><div class="row"><span class="name">Mix Kebab 2,3,6</span><span class="lead"></span><span class="price">€8</span></div><p class="desc">Pieces of chicken tikka &amp; donner meat with garlic mayo, sweet chilli &amp; salad wrapped in naan bread</p></div>
        <div class="item"><div class="row"><span class="name">Garlic Chips</span><span class="lead"></span><span class="price">€4</span></div></div>
        <div class="pics">
          <div class="photo" role="img" aria-label="Photo of samosas with a dipping sauce"></div>
          <div class="photo" role="img" aria-label="Photo of a plated starter with salad"></div>
        </div>
      </div>
    </div>
  </div>

  <div class="panel inner curries">
    <span class="ribbon">Chef Arun's Special Curries</span>
    <div class="cols">
      <div>
        <div class="item"><div class="row"><span class="name">Butter Murgh 3,5</span><span class="lead"></span><span class="price">€10.5</span></div><p class="desc">Chicken cooked in tandoor mixed with rich tomato creamy cashew sauce, splash of cream with hint of honey &amp; dry fenugreek.</p></div>
        <div class="item"><div class="row"><span class="name">Laal Maas</span><span class="lead"></span><span class="price">€11.5</span></div><p class="desc">Traditional rajasthani lamb cooked with garlic and ginger, degi chilli powder, tomatoes finished with star aniseed and clove powder.</p></div>
        <div class="item"><div class="row"><span class="name">Shahi Veg Kofta 3'5</span><span class="lead"></span><span class="price">€10</span></div><p class="desc">Handmade veg and paneer dumplings simmered in tomato sauce, musky fenugreek sauce finished with touch of honey and cream.</p></div>
        <div class="item"><div class="row"><span class="name">Kerala Prawn14</span><span class="lead"></span><span class="price">€12</span></div><p class="desc">Delicacy of kerala spices, tomato and red onion gravy finished with touch of fresh coconut milk.</p></div>
        <div class="item"><div class="row"><span class="name">Punjabi Saag 3 y</span><span class="lead"></span><span class="price">€9.5</span></div><p class="desc">Chicken cooked with spinach, ginger, garlic, fresh cream &amp; tempered with Punjabi tarka.</p></div>
        <div class="item"><div class="row"><span class="name">Royale Korma3, 5</span><span class="lead"></span><span class="price">€8.5</span></div><p class="desc">Breast of chicken cooked in a rich creamy sauce with saffron &amp; coconut, probably most popular among Irish.</p></div>
        <div class="item"><div class="row"><span class="name">Chicken Dahiwala 3</span><span class="lead"></span><span class="price">€9.5</span></div><p class="desc">Amazingly spicy chicken curry cooked with yogurt, green chillies, ginger and herbs.</p></div>
        <div class="item"><div class="row"><span class="name">Murgh Biryani 3,5,y</span><span class="lead"></span><span class="price">€8.5</span></div><p class="desc">Perfumed basmati rice with chicken cubes, nuts, golden onions and biryani spices, served with sauce.</p></div>
      </div>
      <div>
        <div class="item"><div class="row"><span class="name">Masala Hearth Chicken Curry</span><span class="lead"></span><span class="price">€8.5</span></div><p class="desc">Traditional curry cooked with coconut, mustard seed, cashews and curry leaves.</p></div>
        <div class="item"><div class="row"><span class="name">Chicken Karahi</span><span class="lead"></span><span class="price">€8.5</span></div><p class="desc">Boneless chicken prepared in deg with peppers, onion, tomatoes and Indian whole spices.</p></div>
        <div class="item"><div class="row"><span class="name">Chicken Tikka Masala 3</span><span class="lead"></span><span class="price">€8.5</span></div><p class="desc">Chicken roasted in clay oven and simmered in smooth creamy tomato sauce with palm crushed fenugreek leaves and jaggery.</p></div>
        <div class="item"><div class="row"><span class="name">South Indian Garlic Chilli</span><span class="lead"></span><span class="price">€8.5</span></div><p class="desc">Chicken cooked in south Indian style and loaded with garlic, ground spices, fresh herbs</p></div>
        <div class="photo p1" role="img" aria-label="Photo of a curry bowl with fried chicken pieces and mint"></div>
        <div class="photo p2" role="img" aria-label="Photo of a curry dish served with naan bread"></div>
      </div>
    </div>
  </div>

  <div class="panel inner lamb">
    <span class="ribbon">Lamb Dishes</span>
    <div class="cols">
      <div>
        <div class="item"><div class="row"><span class="name">Lamb Madras</span><span class="lead"></span><span class="price">€10.95</span></div><p class="desc">The popular dish of madras cooked with plum tomato, degi chilli, coconut and finished with hint of lemon juice.</p></div>
        <div class="item"><div class="row"><span class="name">Palak Gosht 3, y</span><span class="lead"></span><span class="price">€10.95</span></div><p class="desc">Pan-fried lamb pieces cooked with spinach, fresh herbs, ginger and touch of cream</p></div>
        <div class="item"><div class="row"><span class="name">Lamb Roganjosh</span><span class="lead"></span><span class="price">€10.95</span></div><p class="desc">Slow cooked tender lamb in kashmiri style with fresh herbs and Himalayan spices.</p></div>
        <div class="photo" role="img" aria-label="Photo of a lamb curry with rice"></div>
      </div>
      <div>
        <div class="item"><div class="row"><span class="name">Lamb Kohlapuri</span><span class="lead"></span><span class="price">€10.95</span></div><p class="desc">Cauliflower, potato and broccoli, golden fried with Gram flour batter</p></div>
        <div class="item"><div class="row"><span class="name">Lamb Jalferzi</span><span class="lead"></span><span class="price">€10.95</span></div><p class="desc">Lamb, tossed with cubes of onions, peppers flavored with crushed coriander seeds and dry fenugreek with hint of cream.</p></div>
        <div class="item"><div class="row"><span class="name">Gosht Biryani 3,5,y</span><span class="lead"></span><span class="price">€11.00</span></div><p class="desc">Aged rice cooked with tender land brown onions, home made masala and accompanied with curry sauce.</p></div>
      </div>
    </div>
    <div class="prawn">
      <span class="ribbon">Prawn Dishes</span>
      <div class="cols">
        <div>
          <div class="item"><div class="row"><span class="name">Prawn Masala 3</span><span class="lead"></span><span class="price">€10.95</span></div><p class="desc">Prawns in a smooth creamy sauce flavoured with kasoori methi &amp; tandoori spices.</p></div>
          <div class="item"><div class="row"><span class="name">Prawn Karahi</span><span class="lead"></span><span class="price">€10.95</span></div><p class="desc">Prawns cooked with peppers, spring onion, caramelised onion, tomatoes &amp; whole spices</p></div>
          <div class="item"><div class="row"><span class="name">Goan Prawn Curry3,4,5</span><span class="lead"></span><span class="price">€10.95</span></div><p class="desc">Fisherman's favourite prawn curry aromatic with coconut, mustard, nuts, curry leaves and spices from goa's costal area.</p></div>
        </div>
        <div>
          <div class="item"><div class="row"><span class="name">Prawn Bhuna</span><span class="lead"></span><span class="price">€10.95</span></div><p class="desc">Prawns cooked in onions &amp; tomato with black pepper to bring together the kick of spices</p></div>
          <div class="item"><div class="row"><span class="name">Prawn Biryani 3,6,y</span><span class="lead"></span><span class="price">€10.95</span></div></div>
          <div class="photo" role="img" aria-label="Photo of a prawn curry with rice and spices"></div>
        </div>
      </div>
    </div>
  </div>

  <div class="panel inner veg">
    <span class="ribbon">Vegetarian Dishes</span>
    <div class="cols">
      <div>
        <div class="item"><div class="row"><span class="name">Shahi Paneer 3, 5</span><span class="lead"></span><span class="price">€8.95</span></div><p class="desc">Indian cheese in semi-dry sauce.</p></div>
        <div class="item"><div class="row"><span class="name">Subz Maloni Mild</span><span class="lead"></span><span class="price">€8.95</span></div><p class="desc">Stir fried vegetables with ground spices.</p></div>
        <div class="item"><div class="row"><span class="name">Dum Wale Aloo3</span><span class="lead"></span><span class="price">€8.95</span></div><p class="desc">Potatoes cooked with ginger, garlic, onions, yoghurt &amp; curry leave with cumin flavored.</p></div>
      </div>
      <div>
        <div class="item"><div class="row"><span class="name">Karahi Paneer 3</span><span class="lead"></span><span class="price">€8.95</span></div><p class="desc">Colorful curry is prepared using homemade Indian cheese (paneer)</p></div>
        <div class="item"><div class="row"><span class="name">Saag Paneer</span><span class="lead"></span><span class="price">€8.95</span></div><p class="desc">Pan fried cottage cheese &amp; spinach with kasoori methi &amp; fresh coriander</p></div>
        <div class="item"><div class="row"><span class="name">Vegetable Biryani</span><span class="lead"></span><span class="price">€8.95</span></div><p class="desc">Basmati Rice cooked with vegetables, fresh herbs, spices &amp; fried golden onion. Comes with curry sauce.</p></div>
      </div>
    </div>
    <div class="item" style="width:140px"><div class="row"><span class="name">Sambhar Vegetable Curry 4yv</span></div><div class="row"><span class="desc" style="font-size:5px;line-height:6.6px;font-weight:400">Vegetable curry cooked with lentil, curry leaves, and mustard seeds</span><span class="price">€8.95</span></div></div>
    <div class="nan">
      <span class="ribbon">Nan Bread</span>
      <h4>Side Orders<br>All naan bread contains 2,3,6</h4>
      <div class="list">
        <div class="row"><span class="name">Naan.</span><span class="lead"></span><span class="price">€2.20</span></div>
        <div class="row"><span class="name">Garlic Naan</span><span class="lead"></span><span class="price">€2.50</span></div>
        <div class="row"><span class="name">Garlic Chilli Naan</span><span class="lead"></span><span class="price">€3.00</span></div>
        <div class="row"><span class="name">Peshwari Naan..5</span><span class="lead"></span><span class="price">€2.20</span></div>
        <div class="row"><span class="name">Keema Naan.</span><span class="lead"></span><span class="price">€3.00</span></div>
        <div class="row"><span class="name">Coriander Naan.</span><span class="lead"></span><span class="price">€2.50</span></div>
        <div class="row"><span class="name">Chilli Cheese Naan</span><span class="lead"></span><span class="price">€3.00</span></div>
        <div class="row"><span class="name">G.O.C</span><span class="lead"></span><span class="price">€3.00</span></div>
        <div class="row"><span class="name">Boiled Basmati</span><span class="lead"></span><span class="price">€2.00</span></div>
        <div class="row"><span class="name">Pilau Rice</span><span class="lead"></span><span class="price">€2.00</span></div>
        <div class="row"><span class="name">Lemon Rice</span><span class="lead"></span><span class="price">€2.50</span></div>
      </div>
    </div>
  </div>
</section>

</body>
</html>
```